New Innovative Product needs a new business card design

We need a business card design for a new product line based in Michigan called "Lender TrueCourse." We are a credit company by nature however this product should have a clean, simple, "zorvel-esque" feel. We have a few tag lines we use that could or could not be used...."All Referral Roads Lead to You" we use the attached pic in much or our marketing and also use both a white and/or black logo. Also attached.

We want the image attached on the card in some form or another- the grass/sky image.

Reason: We are extending to go over options with management- (expiring on weekend)

Reason: To finalize our design pick. We will be in touch with the designer of choice within the next day or so...the last few entries have been great- Sorry for the delay.

Reason: Working with a couple different designs trying to get finalized

Reason: Final in the workds

Industry/Entity Type

Marketing

Requirements
Must have
• We want the image attached on the card in some form or another- the grass/sky image.

```html
<!DOCTYPE html>
<html lang="en">
<head>
<meta charset="utf-8">
<title>Lender TrueCourse — Business Card</title>
<link rel="stylesheet" href="https://fonts.googleapis.com/css2?family=Cinzel:wght@400;600&display=swap">
<style>
  :root {
    --backdrop: #e9e9e7;
    --card: #ffffff;
    --ink: #2b2b2b;
    --muted: #444444;
    --green: #1f9a4a;
    --black: #050505;
    --sky-top: #8fc3e8;
    --sky-low: #d7ecf7;
    --grass-top: #6fb24a;
    --grass-low: #3d7f2a;
  }
  * { margin: 0; padding: 0; box-sizing: border-box; }
  html, body { width: 1200px; height: 901px; overflow: hidden; background: var(--backdrop); }
  .stage { position: relative; width: 1200px; height: 901px; }
  .card {
    position: absolute; left: 100px; top: 165px;
    width: 1000px; height: 571px;
    background: var(--card);
    border-radius: 44px;
    overflow: hidden;
    box-shadow: 0 10px 30px rgba(0,0,0,0.15);
    font-family: "Cinzel", Georgia, serif;
  }
  .swoosh { position: absolute; inset: 0; }
  .brand {
    position: absolute; left: 150px; top: 95px;
    width: 440px;
    display: flex; flex-direction: column; align-items: center; gap: 22px;
  }
  .brand-photo {
    width: 150px; height: 110px;
    border-radius: 8px;
    background: linear-gradient(to bottom,
      var(--sky-top) 0%, var(--sky-low) 58%,
      var(--grass-top) 60%, var(--grass-low) 100%);
  }
  .brand-name { font-size: 38px; font-weight: 600; color: var(--ink); letter-spacing: 1px; white-space: nowrap; }
  .contact {
    position: absolute; right: 70px; top: 95px;
    text-align: right; color: var(--muted);
  }
  .person-name { font-size: 27px; color: var(--green); letter-spacing: 2px; }
  .person-title { font-size: 21px; color: var(--muted); letter-spacing: 2px; margin-top: 2px; }
  .address { margin-top: 46px; font-size: 17px; line-height: 28px; letter-spacing: 1px; }
  .lines { margin-top: 40px; list-style: none; font-size: 15px; line-height: 26px; letter-spacing: 1px; }
  .lines li { display: flex; justify-content: flex-end; align-items: center; gap: 10px; }
  .lines svg { width: 14px; height: 14px; fill: var(--green); flex: none; }
</style>
</head>
<body>
<div class="stage">
  <div class="card">
    <svg class="swoosh" viewBox="0 0 1000 571" preserveAspectRatio="none" aria-hidden="true">
      <path d="M0,318 C260,385 620,495 1000,545 L1000,571 L0,571 Z" fill="var(--black)"/>
      <path d="M0,292 C270,360 630,470 1000,520" fill="none" stroke="var(--green)" stroke-width="7"/>
    </svg>

    <div class="brand">
      <div class="brand-photo" role="img" aria-label="Photo of green grass meeting a blue sky"></div>
      <span class="brand-name">Lender TrueCourse</span>
    </div>

    <div class="contact">
      <p class="person-name">Daniel Marsh</p>
      <p class="person-title">President</p>
      <p class="address">214 Harbor Point Drive<br>Lansing MI</p>
      <ul class="lines">
        <li>014 220 5310
          <svg viewBox="0 0 16 16"><path d="M3 1l3 3-1.5 2a9 9 0 0 0 5.5 5.5L12 10l3 3-2 2C7 15 1 9 1 3z"/></svg></li>
        <li>014 220 5310
          <svg viewBox="0 0 16 16"><path d="M4 0h8v16H4zM5.5 2v10h5V2zM7 13.5h2v1H7z" fill-rule="evenodd"/></svg></li>
        <li>014 220 5310
          <svg viewBox="0 0 16 16"><path d="M4 1h6l2 2v3H4zM2 7h12v7H2zM10 9h2v1h-2z"/></svg></li>
        <li>HELLO@TRUECOURSE.COM
          <svg viewBox="0 0 16 16"><path d="M1 3h14v10H1zM2 4l6 5 6-5v-.5H2z" fill-rule="evenodd"/></svg></li>
        <li>WWW.TRUECOURSELEND.COM
          <svg viewBox="0 0 16 16"><path d="M8 1a7 7 0 1 0 0 14A7 7 0 0 0 8 1zm-5.5 7h11M8 1.5c-3 3-3 10 0 13M8 1.5c3 3 3 10 0 13" stroke="#fff" stroke-width="1"/></svg></li>
      </ul>
    </div>
  </div>
</div>
</body>
</html>
```